wardrobe/costume stylist needs good business card for own business

Hi:)

I'm wanting a business card for my company. I am a freelance stylist.

I do wardrobe/costume stylist to TV commercials; Films; Fashion and Lifestyle shoots.

I'd like a design based around my name Rosalind Pember written nicely, maybe a colour? Up to you?!

I've attached a couple of images of business cards I like
.... be creative and have fun!

Thank you :)
Updates

Reason: I was trying to get my new business card ready for before I headed overseas Friday morning but I don't think that was realistic so I'd like to extend the deadline to give time to the project. Thank you

Hi designers:) Thank you for all your designs, I've extended the deadline until Sunday, so there's a bit more time. I've attached 3 pictures of business cards which I quite like, please take a look to see if it can be of help in your process. I like the pale plain or patterned background with dark font and the dark plain or patterned background with the pale font the motifs the feminine fonts the plain fonts I like the idea of playing with a circle or some shape on one side of the card with my name or initials as in the picture I have on my post could you play around with this idea a bit please? Thank you all for the work you've done :) Rosa

Hi I am working overseas til Saturday night sorry for no feedback until I teturn Thanks :) Rosa

Hi designers, Thank you all so much for submitting your designs, I really appreciate your input into my project :) I'm sorry I didn't get to respond to some comments, and give feedback. I didn't back from being away until later than I expected, and the deadline had passed then, so apologies. Thanks to you all again for all your really good designs :) Rosa

Target Market(s)

I am a freelance stylist my target audience is producers, production companies, photographers, directors...

Industry/Entity Type

Business

Requirements
Must have
• Rosalind Pember
Stylist or Wardrobe Stylist

email rosapember@quillnet.co.nz
Mobile 0218846193

(Don't have to use the words 'email' and 'mobile')
Nice to have
• Would like it to be double sided
Like B & W
Like pale colour background with dark font or white font
Like dark colour background with pale font
Should not have
• I would prefer it not to incorporate pictures

```html
<!DOCTYPE html>
<html lang="en">
<head>
<meta charset="utf-8">
<title>Rosalind Pember — Business Card</title>
<link rel="stylesheet" href="https://fonts.googleapis.com/css2?family=Zilla+Slab:wght@300&display=swap">
<style>
  :root {
    --ink: #111111;
    --band: #000000;
    --tint: #e8e6e6;
    --paper: #ffffff;
    --edge: #8a8a8a;
  }
  * { margin: 0; padding: 0; box-sizing: border-box; }
  html, body {
    width: 1200px;
    height: 1000px;
    overflow: hidden;
    background: var(--paper);
  }
  body {
    position: relative;
    font-family: "Zilla Slab", Georgia, serif;
    font-weight: 300;
    color: var(--ink);
  }
  h1, h2, p, ul { font-weight: 300; }
  .card {
    position: absolute;
    top: 241px;
    height: 323px;
    background: var(--paper);
  }
  .card--front {
    left: 13px;
    width: 565px;
    border: 2px solid var(--band);
  }
  .card--back {
    left: 621px;
    width: 564px;
    border: 1px solid var(--edge);
  }
  .card__backdrop {
    position: absolute;
    inset: 0;
  }
  .card--front .card__backdrop {
    background: linear-gradient(153deg,
      var(--band) 0%, var(--band) 7%,
      var(--tint) 12%, var(--tint) 28%,
      var(--paper) 44%, var(--paper) 58%,
      var(--tint) 72%, var(--tint) 88%,
      var(--band) 93%, var(--band) 100%);
  }
  .card--back .card__backdrop {
    background: linear-gradient(27deg,
      var(--tint) 0%, var(--tint) 30%,
      var(--paper) 46%, var(--paper) 60%,
      var(--tint) 76%, var(--tint) 100%);
  }
  .card__content {
    position: absolute;
    inset: 0;
  }
  .name {
    position: absolute;
    right: 155px;
    text-align: right;
    line-height: 1;
    white-space: nowrap;
  }
  .name__first {
    top: 92px;
    font-size: 80px;
    letter-spacing: 1px;
  }
  .name__last {
    top: 172px;
    font-size: 52px;
    letter-spacing: 1px;
  }
  .role {
    position: absolute;
    left: 102px;
    top: 82px;
    font-size: 46px;
    line-height: 1;
    letter-spacing: 1px;
    white-space: nowrap;
  }
  .contact {
    position: absolute;
    left: 110px;
    top: 136px;
    list-style: none;
    font-size: 22px;
    line-height: 25px;
    white-space: nowrap;
  }
  .side-label {
    position: absolute;
    top: 592px;
    font-size: 50px;
    line-height: 1;
    letter-spacing: 1px;
    text-align: center;
    width: 300px;
  }
  .side-label--front { left: 133px; }
  .side-label--back  { left: 758px; }
</style>
</head>
<body>

  <section class="card card--front" aria-label="Card front">
    <div class="card__backdrop" role="img" aria-label="Diagonal black and grey stripe decoration"></div>
    <div class="card__content">
      <h1 class="name name__first">Rosalind</h1>
      <p class="name name__last">Pember</p>
    </div>
  </section>

  <section class="card card--back" aria-label="Card back">
    <div class="card__backdrop" role="img" aria-label="Diagonal grey stripe decoration"></div>
    <div class="card__content">
      <h2 class="role">Wardrobe stylist</h2>
      <ul class="contact">
        <li class="contact__email">RosalindPember@Mailbox.com</li>
        <li class="contact__address">2718 Sample Street, New York</li>
        <li class="contact__phone">1-482-6051</li>
      </ul>
    </div>
  </section>

  <p class="side-label side-label--front">Front</p>
  <p class="side-label side-label--back">Back</p>

</body>
</html>
```